Business Card Design for Massage Therapist

*I am a qualified massage therapist & require a business card for my new business 'Tidal Touch & Wellness'.
*Contact details I'd like included on the card are: Elise Brantry, Mobile: 0481562930, Email: tidaltw@mailvane.com
*It is a massage business dedicated to providing quality therapeutic massage treatments, that will later incorporate natural therapies.
* Styles Include: Swedish, Relaxation, Pregnancy, Deep Tissue & Sports Massage
*I offer the styles of massage as listed above & a mobile service that allows clients to book a massage in the comfort of their own home.
*I'd like my logo to be fairly simple, streamlined, modern & reflect what my business services are - one people will easily remember.
*I'd like the colors to represent & emit a sense of calm, be fresh, welcoming, natural colors that appeal to a wide range of people.
*Colors I'd like to see are: pale blue, aqua & greens.

Target Market(s)

Both Male & Female, aged 20 to 65, singles, couples, parents, business people who are interested in their health, fitness & general wellbeing and maintenance. Located in the Harbourvale area and surrounding suburbs of Melbourne.

Industry/Entity Type

Massage

Requirements
Must have
• Fonts used in logos should be owned by the designer.
Should not have
• I don't want the design to have someone being massaged in it (pictures/photos) or have it look too clinical & sterile.

```html
<!DOCTYPE html>
<html lang="en">
<head>
<meta charset="utf-8">
<title>Tidal Touch &amp; Wellness — Business Card</title>
<link rel="stylesheet" href="https://fonts.googleapis.com/css2?family=Marcellus&family=Arimo&family=Tinos:ital,wght@1,700&family=Archivo+Narrow:wght@500&display=swap">
<style>
  :root {
    --paper: #ffffff;
    --sky-deep: #3fb3e8;
    --sky-mid: #8fd3f3;
    --sky-pale: #d6eefa;
    --brand-grey: #4a4a4a;
    --ink: #111111;
    --name-green: #14a98b;
    --title-teal: #1b6a70;
    --mark-aqua: #1aa98a;
  }
  * { margin: 0; padding: 0; box-sizing: border-box; }
  html, body { width: 1200px; height: 704px; overflow: hidden; background: var(--paper); }
  .card {
    position: relative;
    width: 1200px;
    height: 704px;
    background: var(--paper);
    overflow: hidden;
  }
  .card__wash {
    position: absolute;
    inset: 0;
    background:
      linear-gradient(160deg, var(--sky-deep) 0%, var(--sky-mid) 22%, var(--sky-pale) 42%, rgba(255,255,255,0) 62%),
      linear-gradient(200deg, rgba(143,211,243,0.7) 0%, rgba(214,238,250,0.4) 18%, rgba(255,255,255,0) 35%);
  }
  .brand-top {
    position: absolute;
    left: 0;
    width: 1200px;
    top: 168px;
    text-align: center;
    font-family: "Marcellus", serif;
    font-size: 34px;
    color: var(--brand-grey);
    letter-spacing: 0.3px;
  }
  .brand-side {
    position: absolute;
    left: 100px;
    top: 418px;
    display: flex;
    align-items: center;
    gap: 12px;
    font-family: "Marcellus", serif;
    font-size: 23px;
    color: var(--brand-grey);
  }
  .brand-side__square {
    width: 22px;
    height: 22px;
    background: var(--mark-aqua);
  }
  .details {
    position: absolute;
    left: 100px;
    top: 476px;
    font-family: "Arimo", sans-serif;
    font-size: 25px;
    color: var(--ink);
    list-style: none;
  }
  .details li { height: 45px; line-height: 34px; }
  .therapist {
    position: absolute;
    left: 700px;
    width: 490px;
    top: 432px;
    text-align: center;
  }
  .therapist__name {
    font-family: "Tinos", serif;
    font-style: italic;
    font-weight: 700;
    font-size: 66px;
    line-height: 76px;
    color: var(--name-green);
  }
  .therapist__role {
    font-family: "Archivo Narrow", sans-serif;
    font-weight: 500;
    font-size: 48px;
    line-height: 56px;
    color: var(--title-teal);
  }
</style>
</head>
<body>
  <main class="card">
    <div class="card__wash" role="img" aria-label="Soft pale blue flowing water texture"></div>

    <div class="brand-top">Tidal Touch &amp; Wellness</div>

    <div class="brand-side">
      <span class="brand-side__square"></span>
      <span>Tidal Touch &amp; Wellness</span>
    </div>

    <ul class="details">
      <li>Swedish, Relaxation, Pregnancy.</li>
      <li>Deep Tissue &amp; Sports Massage</li>
      <li>Mobile: 0481 562 930</li>
      <li>E-mail: tidaltw@mailvane.com</li>
    </ul>

    <div class="therapist">
      <div class="therapist__name">Elise Brantry</div>
      <div class="therapist__role">Massage Therapist</div>
    </div>
  </main>
</body>
</html>
```